Art and Artifact Selling classy website.

I am into selling of Art works and artifacts. The art work range from different type such as animation, architecture, assemblage, calligraphy, computer, Christian or religious, conceptual, artistic design, drawing, folk, graffiti, graphic, illuminated manuscript, illustration, mosaic, painting, performance, photography, sculpture. This website will feature categories of the above art works. My website should have images of the above art works and should be classy. My business is based in the United States and my target customers are Americans. Different artistic colors are welcome. My business name is brimwell Art.

Industry/Entity Type

Architecture

Coding

Coded - Design and coding required

```html
<!DOCTYPE html>
<html lang="en">
<head>
<meta charset="utf-8">
<title>Brimwell Art</title>
<link rel="stylesheet" href="https://fonts.googleapis.com/css2?family=Ubuntu:wght@400;500;700&family=Open+Sans:wght@400;600&display=swap">
<style>
:root{
  --orange:#e17e12;
  --dark:#1f1f1f;
  --darker:#2b2b2b;
  --cream:#f6eee4;
  --text:#222;
  --muted:#555;
  --white:#fff;
}
*{margin:0;padding:0;box-sizing:border-box}
html,body{width:789px;height:1200px;overflow:hidden}
body{
  position:relative;
  font-family:"Open Sans",sans-serif;color:var(--text);
  background:
    radial-gradient(ellipse 160px 260px at 0px 330px,#cfe1e8 0%,rgba(207,225,232,0) 100%),
    radial-gradient(ellipse 200px 300px at 789px 820px,#d6e6ea 0%,rgba(214,230,234,0) 100%),
    radial-gradient(ellipse 260px 200px at 500px 60px,#f3ddc2 0%,rgba(243,221,194,0) 100%),
    var(--cream);
}
.abs{position:absolute}
.brand{left:42px;top:24px;font-family:"Ubuntu",sans-serif;font-weight:700;font-size:29px;color:var(--dark);letter-spacing:.3px}
.social{right:42px;top:11px;display:flex;gap:3px}
.social span{width:13px;height:13px;border-radius:50%;background:var(--dark)}
.prefs{left:505px;top:43px;display:flex;align-items:center;font-size:8px;color:#333;gap:6px}
.select{height:17px;border:1px solid #ccc;background:#f4f4f4;display:flex;align-items:center;padding:0 7px;gap:6px;font-size:7.5px}
.swatch{width:10px;height:8px;background:#8a8a8a}
.caret{width:0;height:0;border-left:3px solid transparent;border-right:3px solid transparent;border-top:3px solid #333;margin-left:8px}
.cart{left:719px;top:38px}
.nav{left:40px;top:84px;width:710px;height:32px;background:var(--dark);display:flex;align-items:center}
.nav a{font-family:"Ubuntu",sans-serif;font-weight:500;font-size:10px;color:var(--white);text-decoration:none;letter-spacing:.3px;margin-left:9px;margin-right:27px;position:relative}
.nav a.active::after{content:"";position:absolute;left:0;right:0;bottom:-5px;height:2px;background:var(--orange)}
.search{position:absolute;right:4px;top:3px;width:150px;height:25px;background:var(--white);font-size:9px;color:#999;padding:6px 6px}
.search svg{position:absolute;right:6px;top:5px}
.hero{left:40px;top:116px;width:710px;height:260px;
  background:
    linear-gradient(180deg,rgba(255,255,255,0) 0%,rgba(255,255,255,0) 82%,#cfcfcc 100%),
    linear-gradient(90deg,#3e3e3e 0%,#5a5a5a 20%,#e4e4e2 27%,#4a4a4a 36%,#8c8c8a 45%,#c9c9c7 55%,#e8e8e6 62%,#6a6a6a 72%,#4c4c4c 82%,#d9d9d7 88%,#3a3a3a 94%,#dcdcda 100%)}
.arrow{top:226px;width:24px;height:34px;background:var(--dark);display:flex;align-items:center;justify-content:center}
.cat-head{left:40px;top:377px;width:163px;height:28px;background:var(--dark);color:var(--white);font-family:"Ubuntu",sans-serif;font-size:14px;padding:5px 8px;clip-path:polygon(0 0,152px 0,163px 50%,152px 100%,0 100%)}
.cat-list{left:40px;top:404px;width:151px;height:392px;background:var(--orange);border:1px solid #c96d0c;list-style:none;padding-top:17px}
.cat-list li{font-family:"Ubuntu",sans-serif;font-size:10px;color:var(--white);height:19.4px;padding-left:16px;position:relative}
.cat-list li::before{content:"";position:absolute;left:8px;top:6px;width:2px;height:2px;background:var(--white)}
.cat-list li.current{text-decoration:underline}
.cat-list li.current::after{content:"»";position:absolute;right:10px;top:-1px;font-size:10px}
.side-art{left:40px;top:806px;width:151px;height:160px;
  background:radial-gradient(ellipse 60px 55px at 50% 50%,#6e6a64 0%,#b8b2a8 55%,rgba(232,226,216,0) 100%),linear-gradient(135deg,#efeae2,#ddd6ca)}
.welcome{left:200px;top:412px;width:572px;text-align:center;font-family:"Ubuntu",sans-serif;font-weight:700;font-size:22px;color:#111}
.intro{left:207px;top:452px;width:542px;text-align:center;font-size:8.6px;line-height:14.5px;color:var(--muted)}
.latest{left:206px;top:560px;width:118px;height:23px;background:var(--orange);color:var(--white);font-family:"Ubuntu",sans-serif;font-weight:500;font-size:14px;padding:3px 5px}
.latest-rule{left:206px;top:582px;width:544px;height:1px;background:var(--dark)}
.pager{top:562px;width:13px;height:17px;background:#444;display:flex;align-items:center;justify-content:center}
.product{width:129px;text-align:center}
.product .pic{height:129px;border:2px solid #d6d6d6;position:relative}
.product .name{font-family:"Ubuntu",sans-serif;font-size:10px;margin-top:8px;color:#111}
.product .price{font-size:8px;margin-top:3px;color:#222}
.pic .btn{position:absolute;left:34px;width:63px;height:20px;background:#ececec;font-size:8.5px;line-height:20px;color:#222}
.footer{left:40px;top:1000px;width:710px;height:170px;background:var(--dark);color:var(--white)}
.col{position:absolute;top:24px}
.col h3{font-family:"Ubuntu",sans-serif;font-weight:400;font-size:15px;margin-bottom:9px;white-space:nowrap}
.col ul{list-style:none}
.col li{font-size:9px;line-height:14.5px;padding-left:10px;position:relative}
.col li::before{content:"";position:absolute;left:1px;top:6px;width:3px;height:3px;border-radius:50%;background:var(--white)}
.legal{left:40px;top:1170px;width:710px;height:30px;background:var(--darker);color:var(--white);font-size:8.5px;text-align:center;line-height:30px}
</style>
</head>
<body>

<div class="abs brand">brimwell Art</div>
<div class="abs social"><span></span><span></span><span></span><span></span><span></span></div>

<div class="abs prefs">
  <span>Currency</span>
  <div class="select"><span class="swatch"></span>$ USD<span class="caret"></span></div>
  <div class="select" style="margin-left:1px">Select Language<span class="caret"></span></div>
</div>
<svg class="abs cart" width="24" height="24" viewBox="0 0 24 24">
  <path d="M1 6h4l3 10h11l3-8H7" fill="none" stroke="#111" stroke-width="2.4" stroke-linejoin="round"/>
  <circle cx="10" cy="20" r="2" fill="#111"/><circle cx="18" cy="20" r="2" fill="#111"/>
  <circle cx="19" cy="6" r="5" fill="#e17e12"/>
  <text x="19" y="8.5" font-size="7" fill="#fff" text-anchor="middle" font-family="Open Sans, sans-serif">0</text>
</svg>

<nav class="abs nav">
  <a class="active" href="#">HOME</a><a href="#">PRODUCTS</a><a href="#">ACCESORIES</a><a href="#">LOOKBOOK</a><a href="#">BLOG</a><a href="#">CONTACT</a>
  <div class="search">Search
    <svg width="15" height="15" viewBox="0 0 15 15"><circle cx="6" cy="6" r="4.5" fill="none" stroke="#111" stroke-width="2"/><path d="M9.5 9.5l4.5 4.5" stroke="#111" stroke-width="2.2"/></svg>
  </div>
</nav>

<div class="abs hero" role="img" aria-label="Gallery corner with monochrome paintings of silverware, teapots and a spoon"></div>
<div class="abs arrow" style="left:40px"><svg width="8" height="12"><path d="M7 1L2 6l5 5" fill="none" stroke="#fff" stroke-width="2"/></svg></div>
<div class="abs arrow" style="left:726px"><svg width="8" height="12"><path d="M1 1l5 5-5 5" fill="none" stroke="#fff" stroke-width="2"/></svg></div>

<div class="abs cat-head">Shop by Category</div>
<ul class="abs cat-list">
  <li class="current">Animation</li><li>Architecture</li><li>Assemblage</li><li>Calligraphy</li><li>Computer</li><li>Christian or religious</li><li>Conceptual</li><li>Artistic design</li><li>Drawing</li><li>Folk</li><li>Graffiti</li><li>Graphic</li><li>Illuminated manuscript</li><li>Illustration</li><li>Mosaic</li><li>Painting</li><li>Performance</li><li>Photography</li><li>Sculpture</li>
</ul>
<div class="abs side-art" role="img" aria-label="Ink poster artwork with repeated war lettering on cream paper"></div>

<h1 class="abs welcome">WELCOME TO BRIMWELL ART</h1>
<p class="abs intro">Lorem Ipsum is simply dummy text of the printing and typesetting industry. Lorem Ipsum has been the industry's standard dummy text ever since the 1500s, when an unknown printer took a galley of type and scrambled it to make a type specimen book. It has survived not only five centuries, but also the leap into electronic typesetting, remaining essentially unchanged. It was popularised in the 1960s with the release of Letraset sheets containing Lorem Ipsum passages, and more recently with desktop publishing software like Aldus PageMaker including versions of Lorem Ipsum.</p>

<div class="abs latest">LATEST EDITION</div>
<div class="abs latest-rule"></div>
<div class="abs pager" style="left:721px"><svg width="6" height="9"><path d="M5 1L1.5 4.5 5 8" fill="none" stroke="#fff" stroke-width="1.5"/></svg></div>
<div class="abs pager" style="left:736px"><svg width="6" height="9"><path d="M1 1l3.5 3.5L1 8" fill="none" stroke="#fff" stroke-width="1.5"/></svg></div>

<div class="abs product" style="left:206px;top:599px">
  <div class="pic" role="img" aria-label="Carved wooden antiquity" style="background:radial-gradient(ellipse 40px 60px at 50% 55%,#6b4a30,#4a4642 100%)">
    <div class="btn" style="top:38px">Read more</div><div class="btn" style="top:64px">Add to Cart</div>
  </div>
  <div class="name">All Greek Antiquities</div><div class="price">Price: $25.00</div>
</div>
<div class="abs product" style="left:345px;top:599px">
  <div class="pic" role="img" aria-label="Terracotta relief fragment" style="background:radial-gradient(ellipse 40px 60px at 50% 50%,#c8b79c,#8d7c64 60%,#141414 100%)"></div>
  <div class="name">A-Greek-Terracotta</div><div class="price">Price: $75.00</div>
</div>
<div class="abs product" style="left:483px;top:599px">
  <div class="pic" role="img" aria-label="Carved stone tablet fragment" style="background:radial-gradient(ellipse 45px 60px at 50% 50%,#9a7a58,#6d5238 60%,#0e0e0e 100%)"></div>
  <div class="name">Attic-Black-Figure</div><div class="price">Price: $70.00</div>
</div>
<div class="abs product" style="left:622px;top:599px">
  <div class="pic" role="img" aria-label="Bronze seated animal statuette" style="background:radial-gradient(ellipse 30px 60px at 50% 60%,#3e4c42,#6f7b72 50%,#d0d4d6 100%)"></div>
  <div class="name">Important-Apulian</div><div class="price">Price: $95.00</div>
</div>

<div class="abs product" style="left:206px;top:790px">
  <div class="pic" role="img" aria-label="Gold ornamented figure" style="background:radial-gradient(ellipse 45px 50px at 50% 40%,#d9a63a,#9a6e1e 55%,#262626 100%)"></div>
  <div class="name">Hellenistic-Cornelian</div><div class="price">Price: $25.00</div>
</div>
<div class="abs product" style="left:345px;top:790px">
  <div class="pic" role="img" aria-label="Green stone carved figure" style="background:radial-gradient(ellipse 30px 60px at 50% 50%,#5a6b5c,#34403a 55%,#0b0b0b 100%)"></div>
  <div class="name">All Greek Antiquities</div><div class="price">Price: $75.00</div>
</div>
<div class="abs product" style="left:483px;top:790px">
  <div class="pic" role="img" aria-label="Pair of ceramic figurines" style="background:radial-gradient(ellipse 55px 50px at 50% 55%,#9a5f3c,#b88a6c 55%,#e8e6e2 100%)"></div>
  <div class="name">Attic-Black-Figure</div><div class="price">Price: $70.00</div>
</div>
<div class="abs product" style="left:622px;top:790px">
  <div class="pic" role="img" aria-label="Painted ceramic portrait vessel" style="background:radial-gradient(ellipse 40px 55px at 50% 58%,#b8602e,#7a3c1e 55%,#241610 100%)"></div>
  <div class="name">Important-Apulian</div><div class="price">Price: $95.00</div>
</div>

<footer class="abs footer">
  <div class="col" style="left:31px"><h3>Classical Antiquities</h3>
    <ul><li>Egyptian</li><li>Greek</li><li>Roman</li><li>Near East</li><li>Far East</li><li>Ancient Coins</li></ul></div>
  <div class="col" style="left:201px;top:26px"><h3>Pre-Columbian Art</h3>
    <ul><li>Central America / Caribbean</li><li>Meso America</li><li>South America</li><li>Ancient Textiles</li></ul></div>
  <div class="col" style="left:366px;top:25px"><h3>Services We Provide</h3>
    <ul><li>Valuations &amp; Appraisals</li><li>Estate Liquidation</li><li>Curatorial Consultation</li><li>Translations</li><li>Carbon-14, TL-Testing</li><li>Repairs / Restoration</li><li>Custom Display Stands</li></ul></div>
  <div class="col" style="left:542px;top:26px"><h3>Help Resources</h3>
    <ul><li>Buying</li><li>Selling</li><li>Antiquities Dealer</li><li>Services</li><li>Contact Us</li></ul></div>
</footer>
<div class="abs legal">© 2016 Brimwell Art |Privacy Policy| Terms &amp; Conditions|</div>

</body>
</html>
```